Website re-design

We are a successful furnished apartment provider in Boston. We currently are working on re-designing our website www.ribtenlofts.com to make it more modern, designer look and user friendly. We hired a designer, but are not happy with the designs proposed and want to improve on them. The winning design will be paid regardless of whether we stay with our current designer or not. We want ideas and functional page links to see how it will work. Platform we have chosen is wordpress. Feel free to propose others easy for us to update and modify. We do not like Joomla on which website is currently running. We do not like flash nor long load times.
Please use photos on our website for design presentations. www.ribtenlofts.com

Target Market(s)

doctors, nurses, business men but mostly business women, some post-medical students

Industry/Entity Type

Apartment

Requirements
Must have
• Quick action button for reservation form and a notification and email forwarding system to us of reservation information by potential clients. Blog required with feedback by guests allowed, we can censor which are published. Slide shows of apartments.
Should not have
• No movies.

```html
<!DOCTYPE html>
<html lang="en">
<head>
<meta charset="utf-8">
<title>Ribten Lofts – Furnished Apartments</title>
<link rel="stylesheet" href="https://fonts.googleapis.com/css2?family=Open+Sans:wght@400;600;700&display=swap">
<style>
:root{
  --bg-dark:#2a2a2a;
  --bg-mid:#4a4a4a;
  --gold:#e8c64a;
  --gold-light:#f6e9a6;
  --gold-deep:#a8913e;
  --gold-text:#d9bd4d;
  --panel:rgba(30,30,30,.55);
  --panel-line:#6a6a6a;
  --text:#f2f2f2;
  --muted:#cfcfcf;
  --ink:#2b2614;
}
*{box-sizing:border-box;margin:0;padding:0}
html,body{width:952px;height:1200px;overflow:hidden}
body{
  position:relative;
  font-family:"Open Sans",Arial,sans-serif;
  color:var(--text);
  background:linear-gradient(90deg,#3a3a3a 0%,#555 30%,#4a4a4a 55%,#5a5a5a 75%,#3c3c3c 100%);
}
.abs{position:absolute}
.shadow{position:absolute;height:14px;border-radius:50%;background:radial-gradient(ellipse at center,rgba(0,0,0,.6),rgba(0,0,0,0) 70%)}

/* header */
.brand-plate{left:73px;top:-20px;width:308px;height:126px;border-radius:50%;
  background:radial-gradient(ellipse at 50% 30%,#4b4b4b,#333 70%);box-shadow:0 6px 10px rgba(0,0,0,.5);border:1px solid #666}
.brand{left:102px;top:20px;display:flex;align-items:center;gap:10px}
.brand-dot{width:48px;height:48px;border-radius:50%;background:var(--gold-deep)}
.brand-name{font-size:22px;font-weight:400;color:var(--gold-text);letter-spacing:2px;line-height:1}
.brand-tag{font-size:9.5px;color:var(--gold-text);letter-spacing:1.2px;margin-top:4px}
.help{left:618px;top:17px;width:265px;height:52px;border-radius:10px;border:1px solid #888;background:#333;box-shadow:0 3px 6px rgba(0,0,0,.5)}
.help-ask{left:100px;top:4px;font-size:12px;font-weight:700;color:var(--gold-text);letter-spacing:1px}
.help-phone{left:84px;top:20px;font-size:23px;font-weight:700;color:#fff;letter-spacing:1px}

/* nav */
.nav{left:73px;top:128px;width:810px;height:37px;border-radius:14px;
  background:linear-gradient(#f8eeb8,#e0cb7a 50%,#c6ad55);display:flex;align-items:center;overflow:hidden;box-shadow:0 3px 6px rgba(0,0,0,.5)}
.nav a{font-size:11px;color:var(--ink);text-decoration:none;flex:1;text-align:center;border-left:1px dotted #a89550;line-height:37px}
.nav a.current{flex:0 0 69px;margin-left:13px;background:linear-gradient(#666,#222);color:#fff;border:none}
.nav a.current + a{border-left:none}

/* sidebar */
.side{left:77px;top:194px;width:229px;height:365px;border-radius:8px;border:1px solid #c9b76a;
  background:linear-gradient(#f7eaad,#d9c268 60%,#b39a45)}
.side ul{list-style:none;padding:12px 13px 0 10px}
.side li{font-size:11px;color:var(--ink);height:30px;line-height:30px;padding-left:22px;border-bottom:1px dotted #a89550}
.side li.active{background:linear-gradient(#fff,#e8e8e8);margin:0 -13px 0 -10px;padding-left:32px;border:none;position:relative}
.side li.active svg{position:absolute;left:6px;top:5px}
.side li:last-child{border:none}

/* slider */
.slider{left:327px;top:187px;width:548px;height:373px;border:1px solid #777;background:#3a3a3a}
.slide-photo{left:8px;top:8px;width:532px;height:355px;background:linear-gradient(160deg,#c6b28f,#8a6a45 55%,#3b2f4a)}
.slide-text{left:14px;top:24px;font-size:17px;line-height:25px;color:#fff;width:400px}
.thumbs{left:8px;top:258px;width:532px;height:105px;background:rgba(40,40,40,.75);border-top:1px solid #777}
.thumb{position:absolute;top:19px;width:110px;height:75px;border:2px solid #fff}
.arrow{position:absolute;top:333px}

/* welcome */
.ring{left:77px;top:598px;width:186px;height:186px;border-radius:50%;background:#222;box-shadow:0 4px 10px rgba(0,0,0,.5)}
.ring-photo{left:9px;top:9px;width:168px;height:168px;border-radius:50%;background:linear-gradient(150deg,#e0c98f,#a97f4f 60%,#5e6b85)}
.welcome{left:267px;top:617px;width:389px}
.welcome h1{font-size:15.5px;font-weight:400;margin-bottom:6px;white-space:nowrap}
.welcome h1 b,.hl{color:var(--gold);font-weight:700}
.copy{font-family:Arial,sans-serif;font-size:9.6px;line-height:13.3px;color:var(--muted);text-align:justify}
.copy strong{color:#fff}
.like{margin-top:12px;font-family:Arial,sans-serif;font-size:9.6px;color:var(--gold-text)}
.like strong{color:#fff}

/* reserve */
.reserve{left:683px;top:604px;width:197px;height:65px;border-radius:10px;border:1px solid #ddd;
  background:linear-gradient(#faf4d6,#e2cf85 50%,#b79c40);display:flex;align-items:center;justify-content:center;gap:6px;text-decoration:none}
.reserve .r{font-size:19px;font-weight:700;color:#3a3a3a;letter-spacing:2px}
.reserve .n{font-size:28px;font-weight:700;color:#fff;letter-spacing:2px}

.info{left:677px;top:708px;width:207px;height:261px;border-radius:10px;border:1px solid #777;background:var(--panel)}
.info h2{position:absolute;left:11px;top:10px;font-size:14px;font-weight:400}
.info-photo{left:11px;top:40px;width:186px;height:96px;border:3px solid #fff;background:linear-gradient(150deg,#d8c6a0,#8f6b45 60%,#5b6a82)}
.info .copy{position:absolute;left:7px;top:146px;width:193px}
.more{right:6px;bottom:8px;font-family:Arial,sans-serif;font-size:9.6px;color:var(--gold-text);font-weight:700}

.follow{left:679px;top:1004px;width:195px;height:64px;border-radius:10px;border:1px solid #777;background:var(--panel);text-align:center}
.follow h3{font-size:14px;font-weight:400;margin-top:4px}
.follow h3 b{font-weight:700}
.socials{display:flex;justify-content:center;gap:18px;margin-top:6px}
.socials span{width:24px;height:24px;border-radius:50%}

/* blog */
.post{left:95px;top:816px;width:561px;height:263px;border:1px solid #666;background:var(--panel)}
.post h2{position:absolute;left:9px;top:2px;font-size:14.5px;font-weight:400}
.post .cats{position:absolute;left:9px;top:22px;font-size:10.5px;color:var(--gold)}
.post .meta{position:absolute;left:10px;top:37px;font-family:Arial,sans-serif;font-size:10px}
.post .copy{position:absolute;left:10px;top:71px;width:300px;text-align:left}
.post .by{position:absolute;left:10px;top:213px;font-family:Arial,sans-serif;font-size:10px;color:var(--gold-text)}
.post .by span{color:#fff}
.share{position:absolute;left:7px;top:231px;display:flex;align-items:center;gap:9px;font-family:Arial,sans-serif;font-size:10px}
.share i{width:15px;height:15px;display:block;border-radius:2px}
.share .row{display:flex;gap:1px}
.share .row i{background:#ddd;border:1px solid #888;width:15px;height:14px;border-radius:0}
.post-photo{left:316px;top:21px;width:231px;height:220px;border:3px solid #fff;background:linear-gradient(160deg,#c99552,#7d5530 50%,#e6dccf)}
.date{left:51px;top:846px;width:44px;height:51px;border-radius:5px;border:1px solid #ddd;background:linear-gradient(#f8efc4,#c9b05a);text-align:center;font-family:Arial,sans-serif;color:#fff;line-height:1}
.date .d{font-size:12px;margin-top:4px}
.date .m{font-size:15px;font-weight:700}
.date .y{font-size:11px}

/* footer */
.footer{left:0;top:1126px;width:952px;height:74px;background:#1f1f1f;border-top:1px solid #444}
.footer nav{position:absolute;left:75px;top:21px;font-size:11px}
.footer nav a{color:#fff;text-decoration:none}
.footer nav em{font-style:normal;margin:0 8px}
.copyright{position:absolute;left:73px;top:46px;font-family:Arial,sans-serif;font-size:10px;color:#ddd}
</style>
</head>
<body>

<header>
  <div class="abs brand-plate"></div>
  <div class="abs brand">
    <span class="brand-dot"></span>
    <div>
      <div class="brand-name">RIBTEN LOFTS</div>
      <div class="brand-tag">FURNISHED APARTMENTS</div>
    </div>
  </div>
  <div class="abs help">
    <svg class="abs" style="left:12px;top:4px" width="62" height="44" viewBox="0 0 62 44" aria-hidden="true">
      <path d="M8 8 L54 2 L58 34 L12 40 Z" fill="#2aa3d6"/>
      <path d="M8 8 L34 24 L54 2" fill="none" stroke="#9fdcf3" stroke-width="2"/>
    </svg>
    <div class="abs help-ask">can we help you??</div>
    <div class="abs help-phone">555 010 0199</div>
  </div>
  <nav class="abs nav">
    <a class="current" href="#">Home</a><a href="#">Apartments</a><a href="#">Reservations</a><a href="#">Blog</a><a href="#">Reviews</a><a href="#">Contact</a><a href="#">Boston</a><a href="#">About Us</a>
  </nav>
</header>

<aside class="abs side">
  <ul>
    <li class="active"><svg width="20" height="20" viewBox="0 0 20 20" aria-hidden="true"><circle cx="10" cy="10" r="9" fill="#ddd" stroke="#999"/><path d="M5 6l4 4-4 4M10 6l4 4-4 4" stroke="#555" stroke-width="2" fill="none"/></svg>Contact</li>
    <li>Apartments</li><li>Reservations</li><li>Links</li><li>Locations</li><li>Rates</li><li>Blog</li><li>Chirpline</li><li>Reviews</li><li>Boston</li><li>About Us</li>
  </ul>
</aside>
<div class="shadow" style="left:95px;top:565px;width:200px"></div>

<section class="abs slider">
  <div class="abs slide-photo" role="img" aria-label="Furnished living room with armchairs, bed and tall windows"></div>
  <div class="abs slide-text">Ribten Lofts is proud to offer some of the best furnished apartments in Boston.</div>
  <div class="abs thumbs">
    <div class="thumb" style="left:15px;background:linear-gradient(150deg,#c9a77a,#6d5a66)" role="img" aria-label="Bedroom thumbnail"></div>
    <div class="thumb" style="left:146px;background:linear-gradient(150deg,#cfc3ad,#6e5236)" role="img" aria-label="Living room thumbnail"></div>
    <div class="thumb" style="left:276px;background:linear-gradient(150deg,#e6e2da,#6e4e33)" role="img" aria-label="Kitchen thumbnail"></div>
    <div class="thumb" style="left:407px;background:linear-gradient(150deg,#d9cbb0,#5d6d8a)" role="img" aria-label="Sitting area thumbnail"></div>
  </div>
</section>
<svg class="arrow" style="left:315px" width="34" height="78" viewBox="0 0 34 78" aria-hidden="true"><path d="M30 0 C4 20 0 58 30 78 C20 58 20 20 30 0Z" fill="#eee"/><path d="M8 39 L24 27 V51 Z" fill="#e3cf1b"/></svg>
<svg class="arrow" style="left:853px" width="34" height="78" viewBox="0 0 34 78" aria-hidden="true"><path d="M4 0 C30 20 34 58 4 78 C14 58 14 20 4 0Z" fill="#eee"/><path d="M26 39 L10 27 V51 Z" fill="#e3cf1b"/></svg>
<div class="shadow" style="left:350px;top:566px;width:500px"></div>

<section>
  <div class="abs ring"><div class="abs ring-photo" role="img" aria-label="Sunny sitting room with armchairs"></div></div>
  <div class="abs welcome">
    <h1>Welcome to <b>RIBTEN LOFTS FURNISHED</b> Apartments</h1>
    <p class="copy"><strong>Ribten Lofts is proud to offer some of the best furnished apartments in Boston. Our locations are in the trendiest area</strong> of the city: the South End. In the South End neighborhood, you will find wonderful restaurants, theaters, cafes and artist lofts. Our short term and extended stay apartments are very, very clean. We also offer the latest designer layouts: hardwood floors, Wireless Dsl, Cable TV, flat screen in most apartments, washer and dryer, cookware, cotton linens. Please click links on left for photo galleries, pricing, availability and</p>
    <p class="like">If you are on Linkbook, please <strong>"like" us!</strong></p>
  </div>
</section>

<aside>
  <a class="abs reserve" href="#"><span class="r">RESERV</span><span class="n">NOW</span></a>
  <div class="shadow" style="left:700px;top:675px;width:160px"></div>
  <div class="abs info">
    <h2>Reservation <span class="hl">Information</span></h2>
    <div class="abs info-photo" role="img" aria-label="Apartment with fireplace and dining table"></div>
    <p class="copy"><strong>Ribten Lofts is proud to offer some of the best furnished apartments</strong> in Boston. Our locations are in the trendiest area of the city: the South End. In the South End neighborhood, you will find wonderful restaurants, theaters,</p>
    <span class="abs more">Readmore [+]</span>
  </div>
  <div class="shadow" style="left:700px;top:975px;width:160px"></div>
  <div class="abs follow">
    <h3>follow <b>Us on :</b></h3>
    <div class="socials"><span style="background:#e4631b"></span><span style="background:#39a9de"></span><span style="background:#2d4f9e"></span></div>
  </div>
  <div class="shadow" style="left:695px;top:1073px;width:160px"></div>
</aside>

<article>
  <div class="abs date"><div class="d">16</div><div class="m">Dec</div><div class="y">2011</div></div>
  <div class="abs post">
    <h2>Corporate Apartment design evolution</h2>
    <div class="cats">News from Ribten / Latest News - Ribten Lofts / Elm Row</div>
    <div class="meta">Posted on September 15, 2011 by admin</div>
    <p class="copy"><strong>Ribten Lofts is proud to offer some of the best furnished apartments in Boston. Our locations are in the trendiest area</strong> of the city: the South End. In the South End neighborhood, you will find wonderful restaurants, theaters, cafes and artist lofts. Our short term and extended stay apartments are very, very clean. We also offer the latest designer layouts: hardwood floors, Wireless Dsl, Cable TV, flat screen in most apartments, washer and dryer, cookware, cotton linens. Please click links on left for photo galleries, pricing, availability and</p>
    <div class="by">Blog Psted By <span>Dana Morrow</span></div>
    <div class="share">
      <i style="background:#5a9e3a;border-radius:50%"></i><i style="background:#4a7fd6"></i><i style="background:#e08a2b"></i><i style="background:#c33"></i>
      <span>Share This</span>
      <span class="row"><i></i><i></i><i></i><i></i></span>
    </div>
    <div class="abs post-photo" role="img" aria-label="Bright bedroom with white bed and desk"></div>
  </div>
</article>

<footer class="abs footer">
  <nav><a href="#">Home</a><em>|</em><a href="#">Apartments</a><em>|</em><a href="#">Reservations</a><em>|</em><a href="#">Blog</a><em>|</em><a href="#">Reviews</a><em>|</em><a href="#">Contact</a><em>|</em><a href="#">Boston</a><em>|</em><a href="#">About Us</a></nav>
  <div class="copyright">© Ribten Lofts 2010 - All Rights Reserved &nbsp;Privacy Policy and Terms of Uses</div>
</footer>

</body>
</html>
```